Company providing Business Management Services needs modern business card

The business provides services like tender preparation, bank submissions, business health checks, financial and admin support. We want to portray 'Trust', 'Strength' and 'Support'.
2 styles of logo in various formats have been uploaded.
Looking for easy to understand, yet sophisticated and stand out from the crowd.

Target Market(s)

Small and Medium sized businesses

Industry/Entity Type

Business

Contact Information for Business Card

Name - Daniel Vesterby, Description - Manager, Phone - 0472 915 603, Email - danielvesterby@kpwholdingsgroup.example, Work description - Business Management Services.

Requirements
Must have
• Logo

```html
<!DOCTYPE html>
<html lang="en">
<head>
<meta charset="utf-8">
<title>KPW Holdings Group – Business Card</title>
<link rel="stylesheet" href="https://fonts.googleapis.com/css2?family=Roboto+Condensed:wght@400&display=swap">
<style>
  :root {
    --backdrop: #0d0d0d;
    --card: #ffffff;
    --ink: #111111;
    --brand-grey: #4a4a4a;
    --purple: #9b4f9e;
    --blue: #2e5ea8;
    --green: #4caf50;
    --orange: #f07b22;
  }
  * { margin: 0; padding: 0; box-sizing: border-box; }
  html, body {
    width: 1200px; height: 900px; overflow: hidden;
    background: var(--backdrop);
    font-family: "Roboto Condensed", "Arial Narrow", sans-serif;
    color: var(--ink);
  }
  .card {
    position: absolute; left: 122px; top: 165px;
    width: 955px; height: 573px;
    background: var(--card);
  }
  .holder {
    position: absolute; right: 80px; top: 92px;
    text-align: right;
  }
  .holder-name { font-size: 37px; line-height: 1; letter-spacing: -0.3px; }
  .holder-role { font-size: 20px; margin-top: 6px; }

  .contacts { position: absolute; left: 0; top: 270px; list-style: none; }
  .contact-row {
    display: flex; align-items: center;
    height: 32px; margin-bottom: 8px;
    font-size: 20px;
  }
  .contact-icon {
    width: 66px; height: 32px;
    display: flex; align-items: center; justify-content: center;
    margin-right: 15px;
  }
  .contact-icon svg { width: 18px; height: 18px; fill: none; stroke: #fff; stroke-width: 2; }
  .icon-address { background: var(--purple); }
  .icon-phone { background: var(--blue); }
  .icon-email { background: var(--green); }
  .icon-web { background: var(--orange); }

  .brand {
    position: absolute; left: 463px; top: 258px;
    width: 420px;
  }
  .brand-mark {
    display: flex; align-items: center; gap: 18px;
  }
  .brand-square {
    width: 56px; height: 56px; background: var(--brand-grey);
  }
  .brand-name {
    font-size: 44px; color: var(--brand-grey); line-height: 1;
    letter-spacing: 0.5px;
  }
  .brand-tagline {
    margin-top: 74px; margin-left: 141px;
    font-size: 21px;
  }
</style>
</head>
<body>
  <main class="card">
    <header class="holder">
      <h1 class="holder-name" style="font-weight:400">Daniel Vesterby</h1>
      <p class="holder-role">Manager</p>
    </header>

    <ul class="contacts">
      <li class="contact-row">
        <span class="contact-icon icon-address">
          <svg viewBox="0 0 24 24"><path d="M12 22s-7-7.5-7-13a7 7 0 0 1 14 0c0 5.5-7 13-7 13z" fill="#fff" stroke="none"/><circle cx="12" cy="9" r="2.6" fill="#9b4f9e" stroke="none"/></svg>
        </span>
        <span>418 Harlow Street, Brookfield 60214</span>
      </li>
      <li class="contact-row">
        <span class="contact-icon icon-phone">
          <svg viewBox="0 0 24 24"><path d="M3 9c0-3 4-5 9-5s9 2 9 5l-4 1-1-3H8L7 10z" fill="#fff" stroke="none"/><rect x="5" y="12" width="14" height="8" rx="1" fill="#fff" stroke="none"/></svg>
        </span>
        <span>0472 915 603</span>
      </li>
      <li class="contact-row">
        <span class="contact-icon icon-email">
          <svg viewBox="0 0 24 24"><rect x="3" y="6" width="18" height="12"/><path d="M3 6l9 7 9-7"/></svg>
        </span>
        <span>danielvesterby@kpwholdingsgroup.example</span>
      </li>
      <li class="contact-row">
        <span class="contact-icon icon-web">
          <svg viewBox="0 0 24 24"><path d="M10 14l4-4"/><path d="M8 12l-3 3a3 3 0 0 0 4 4l3-3"/><path d="M16 12l3-3a3 3 0 0 0-4-4l-3 3"/></svg>
        </span>
        <span>www.kpwholdings.example</span>
      </li>
    </ul>

    <section class="brand">
      <div class="brand-mark">
        <span class="brand-square"></span>
        <span class="brand-name">KPW Holdings Group</span>
      </div>
      <p class="brand-tagline">Business Management Services</p>
    </section>
  </main>
</body>
</html>
```